Business Card & Logo Design - Hedge Fund

We need a business card and logo design for a hedge fund. The hedge fund is named Morvane Equity LLC. Morvane Equity was created by finance professors and the strategy is based academic research that looks for patterns in stock prices. The design should look conservative, solid, strong. We favor a classic style - nothing flashy. The logo can relate to the name Morvane Equity, or it could involve a symbol design that connotes "science" . We are open to ideas. We do not want alot of colors - but if any, color - blue is preferred. The font that seems to look best for the name (Morvane Equity) is arial black. We are open to ideas. Most important - we want to see a mock up of an actual business card with the logo concept embedded. The business card should include space for : company name, individual name, position title, cell phone, address. We hope to have this work done by Sept. 8.

Target Market(s)

We will be meeting with and giving the business card to institutions and high net worth individuals.

Industry/Entity Type

Investment Advisory

Contact Information for Business Card

Company name - Morvane Equity LLC
Individual name - Peter Dalby
Title - Portfolio Manager
Cell - (412) 555-0187
Address - 2650 Birchmont Lane, Suite 300, Atlanta GA 30327

Font styles to use
Other font styles liked:
• Arial

Colors
3277b5
0255a3
85acd3
cedeed
fdf9cf
d9d9d9
e6e6e6
f04a50
6b449b

Requirements
Must have
• Must have card details that are sited above.
• We would like a logo related to the name (Morvane Equity) or concept of the fund.
Nice to have
• We want conservative / understated / clean crisp look.
• If any colors - we prefer conservative appearance - blue / gray.
• I have enclosed an example of a card style that looks attractive - please do not exactly copy this card. This is not our company or logo. I feel the layout is attractive - just as an example
Should not have
• Avoid too much color.
• I have selected some preferred colors. Please do not use all of the colors - I have selected a few that might work - but I am not sure. We are open to your ideas so please do not feel the need to use all or any of these.

```html
<!DOCTYPE html>
<html lang="en">
<head>
<meta charset="utf-8">
<title>Morvane Equity LLC – Business Card</title>
<link rel="stylesheet" href="https://fonts.googleapis.com/css2?family=Arimo:wght@400;700&display=swap">
<style>
  :root {
    --backdrop: #d2d2d2;
    --card: #ffffff;
    --brand-blue: #0a50a8;
    --ghost: #f1f1f1;
    --ink-soft: #7a7a7a;
    --on-blue: #ffffff;
  }
  * { margin: 0; padding: 0; box-sizing: border-box; }
  html, body {
    width: 1200px;
    height: 800px;
    overflow: hidden;
    background: var(--backdrop);
    font-family: "Arimo", Arial, sans-serif;
  }
  .stage {
    width: 1200px;
    height: 800px;
    display: flex;
    align-items: center;
    justify-content: center;
  }
  .business-card {
    position: relative;
    width: 840px;
    height: 480px;
    background: var(--card);
    overflow: hidden;
    box-shadow: 0 6px 18px rgba(0,0,0,0.12);
  }
  .ghost-mark {
    position: absolute;
    left: 130px;
    top: 20px;
    width: 400px;
    height: 400px;
    border-radius: 50%;
    background: var(--ghost);
  }
  .corner-block {
    position: absolute;
    left: 0;
    top: 48px;
    width: 120px;
    height: 100px;
    background: var(--brand-blue);
  }
  .brand {
    position: absolute;
    left: 136px;
    top: 66px;
    display: flex;
    align-items: center;
    gap: 14px;
  }
  .brand-dot {
    width: 64px;
    height: 64px;
    border-radius: 50%;
    border: 7px solid var(--brand-blue);
    background: var(--card);
    flex-shrink: 0;
  }
  .brand-name {
    font-weight: 700;
    font-size: 38px;
    color: var(--brand-blue);
    letter-spacing: 0.3px;
    white-space: nowrap;
  }
  .name-band {
    position: absolute;
    left: 410px;
    top: 170px;
    right: 0;
    height: 92px;
    background: var(--brand-blue);
    padding: 14px 0 0 28px;
    color: var(--on-blue);
  }
  .person-name {
    font-weight: 700;
    font-size: 34px;
    line-height: 1.1;
  }
  .person-title {
    font-size: 18px;
    margin-top: 4px;
  }
  .contact {
    position: absolute;
    left: 410px;
    top: 282px;
    color: var(--ink-soft);
    font-size: 26px;
    line-height: 1.35;
    list-style: none;
  }
  .contact li {
    display: flex;
    align-items: flex-start;
    gap: 6px;
  }
  .contact svg {
    flex-shrink: 0;
    margin-top: 5px;
  }
</style>
</head>
<body>
<main class="stage">
  <article class="business-card">
    <div class="ghost-mark" aria-hidden="true"></div>
    <div class="corner-block" aria-hidden="true"></div>

    <div class="brand">
      <span class="brand-dot" aria-hidden="true"></span>
      <span class="brand-name">Morvane Equity LLC</span>
    </div>

    <div class="name-band">
      <p class="person-name">Peter Dalby</p>
      <p class="person-title">Portfolio Manager</p>
    </div>

    <ul class="contact">
      <li>
        <svg width="18" height="24" viewBox="0 0 18 24" aria-hidden="true">
          <rect x="2" y="1" width="14" height="22" rx="2.5" fill="none" stroke="var(--brand-blue)" stroke-width="2.5"/>
          <rect x="6" y="18" width="6" height="2" fill="var(--brand-blue)"/>
        </svg>
        <span>(412) 555-0187</span>
      </li>
      <li>
        <svg width="18" height="24" viewBox="0 0 18 24" aria-hidden="true">
          <path d="M9 1a8 8 0 0 0-8 8c0 6 8 14 8 14s8-8 8-14a8 8 0 0 0-8-8z" fill="var(--brand-blue)"/>
          <circle cx="9" cy="9" r="3.2" fill="#fff"/>
        </svg>
        <span>2650 Birchmont Lane,<br>Suite 300, Atlanta GA 30327</span>
      </li>
    </ul>
  </article>
</main>
</body>
</html>
```